Bright Tooth Dentistry Business Card

We need business cards for our dental office.
We are looking for a clean, elegant design

We provide dental services to children.
Our card needs to be appealing to referring dentists, parents and our team

Target Market(s)

referring dentists, parents and our team

Industry/Entity Type

Dental Clinic

Contact Information for Business Card

4816 Juniper Lane, Suite 240
Cedar Hollow, PA 15237

412-837-2961 Voice
412-837-2962 fax
info@brighttoothdentalpa.com email
www.brighttoothdentalpa.com web

Font styles to use
Sans Serif

Requirements
Must have
• White background - clean, crisp, elegant, simple
• rounded corners
• different color palate - once we come up with design, we will replace the blue with orange, green,
Nice to have
• Follow our logo typeface and colors
• then we can replace color

```html
<!DOCTYPE html>
<html lang="en">
<head>
<meta charset="utf-8">
<title>Bright Tooth Dentistry – Business Card</title>
<link href="https://fonts.googleapis.com/css2?family=Open+Sans:wght@400;600&display=swap" rel="stylesheet">
<style>
  :root {
    --stage: #2d2d2d;
    --card-white: #ffffff;
    --brand-blue: #1ca7e6;
    --deep-blue: #0b6a91;
    --band-gray: #a7a9ac;
    --stripe-gray: #a9abae;
    --ink: #1f1f1f;
  }
  * { margin: 0; padding: 0; box-sizing: border-box; }
  html, body { width: 1200px; height: 1000px; overflow: hidden; }
  body {
    background: var(--stage);
    font-family: "Open Sans", Arial, sans-serif;
    position: relative;
  }
  .card {
    position: absolute;
    border-radius: 12px;
    overflow: hidden;
    background: var(--card-white);
  }
  /* Front */
  .card-front { left: 268px; top: 70px; width: 664px; height: 375px; }
  .front-name {
    position: absolute; left: 0; right: 0; top: 225px;
    text-align: center;
    font-size: 48px; font-weight: 600;
    color: var(--brand-blue);
    letter-spacing: -0.5px;
  }
  .front-mark {
    position: absolute; left: 307px; top: 110px;
    width: 50px; height: 50px; border-radius: 50%;
    background: var(--brand-blue);
  }
  .web-band {
    position: absolute; left: 0; right: 0; bottom: 0; height: 32px;
    background: var(--band-gray);
    color: var(--card-white);
    font-size: 19px; line-height: 32px; text-align: center;
    letter-spacing: 0.3px;
  }
  /* Back */
  .card-back { left: 265px; top: 515px; width: 668px; height: 377px; background: var(--deep-blue); }
  .back-shapes { position: absolute; inset: 0; }
  .back-name {
    position: absolute; left: 16px; top: 82px;
    font-size: 16.5px; font-weight: 600;
    color: var(--brand-blue);
    white-space: nowrap;
  }
  .contact-list { position: absolute; left: 0; top: 0; width: 100%; height: 100%; list-style: none; }
  .contact-item {
    position: absolute; left: 303px;
    font-size: 18px; line-height: 29px; color: var(--ink);
    white-space: nowrap;
  }
  .contact-item svg { position: absolute; left: -70px; top: 5px; }
  .contact-text { display: block; }
</style>
</head>
<body>

  <section class="card card-front" aria-label="Business card front">
    <span class="front-mark" aria-hidden="true"></span>
    <h1 class="front-name">Bright Tooth Dentistry</h1>
    <div class="web-band">www.brighttoothdentalpa.com.web</div>
  </section>

  <section class="card card-back" aria-label="Business card back">
    <svg class="back-shapes" width="668" height="377" viewBox="0 0 668 377" aria-hidden="true">
      <path d="M238,0 L628,0 C652,150 646,280 618,377 L178,377 C176,250 198,100 238,0 Z" fill="var(--stripe-gray)"/>
      <path d="M246,0 L608,0 C640,150 636,280 612,377 L198,377 C188,250 212,100 246,0 Z" fill="var(--brand-blue)"/>
      <path d="M252,0 L557,0 C614,120 624,260 602,377 L210,377 C200,260 214,100 252,0 Z" fill="var(--card-white)"/>
    </svg>

    <div class="back-name">Bright Tooth Dentistry</div>

    <ul class="contact-list">
      <li class="contact-item" style="top:140px">
        <svg width="20" height="32" viewBox="0 0 20 32" aria-hidden="true">
          <path d="M10 1C5 1 1 5 1 10c0 7 9 17 9 17s9-10 9-17c0-5-4-9-9-9z" fill="var(--brand-blue)"/>
          <circle cx="10" cy="10" r="3.5" fill="#fff"/>
        </svg>
        <span class="contact-text">4816 Juniper Lane, Suite 240</span>
        <span class="contact-text">Cedar Hollow, PA 15237</span>
      </li>
      <li class="contact-item" style="top:228px">
        <svg width="24" height="20" viewBox="0 0 24 20" aria-hidden="true">
          <path d="M2 6c0-3 20-3 20 0v2h-5V6H7v2H2z" fill="var(--brand-blue)"/>
          <path d="M6 9h12l3 9H3z" fill="var(--brand-blue)"/>
          <circle cx="12" cy="13" r="2.5" fill="#fff"/>
        </svg>
        <span class="contact-text">412.837.2961</span>
      </li>
      <li class="contact-item" style="top:258px">
        <svg width="24" height="22" viewBox="0 0 24 22" aria-hidden="true">
          <rect x="6" y="1" width="12" height="7" fill="none" stroke="var(--brand-blue)" stroke-width="2"/>
          <rect x="1" y="8" width="22" height="10" rx="2" fill="var(--brand-blue)"/>
          <rect x="6" y="14" width="12" height="7" fill="#fff" stroke="var(--brand-blue)" stroke-width="2"/>
        </svg>
        <span class="contact-text">412.837.2962</span>
      </li>
      <li class="contact-item" style="top:288px">
        <svg width="24" height="18" viewBox="0 0 24 18" aria-hidden="true">
          <rect x="1" y="1" width="22" height="16" fill="none" stroke="var(--brand-blue)" stroke-width="1.6"/>
          <path d="M1 1l11 9 11-9M1 17l8-7M23 17l-8-7" fill="none" stroke="var(--brand-blue)" stroke-width="1.6"/>
        </svg>
        <span class="contact-text">info@brighttoothdentalpa.com</span>
      </li>
    </ul>
  </section>

</body>
</html>
```